Business Card Design

I am after a business card design to be made for my pet care business in Darwin, Northern Territory Australia called Merrily Mutts. I am a certified canine trainer and offer training classes from puppy love class, basic obedience classes, intermediate classes, private lessons, mobile dog wash and grooming and pet minding. I currently have a logo that I would like used on the card that incorporates different shades of orange with the writing in black. I really want my card to stand out from the rest and look professional, easy to read with 'the edge' factor. Im thinking both sides printed on with contact details on one side and services provided on the back
Updates

Thank you all so much for your time. I am overwhelmed with designs as they are all 

really great. My business partner and myself have shortlisted a few that really caught our eye and
Will update as soon as we decide. 

Once again thank you to you all for your great designs :)

Industry/Entity Type

Training

Contact Information for Business Card

Merrily Mutts
merrilymutts@postlark.example
merrilymutts.example.au
0437260000
pet minding
Puppy classes
basic obedience classes
intermediate obedience classes
private lessons
mobile dog wash and grooming
certified dog trainer
CDTQ certified
Police checked
fully insured
honest
reliable
find us on facebook www.socialnook.example/merrilymutts

Requirements
Must have
• My current logo either the stacked version or side by side - whatever works best and must include my services

```html
<!DOCTYPE html>
<html lang="en">
<head>
<meta charset="utf-8">
<title>Merrily Mutts – Business Card</title>
<link rel="stylesheet" href="https://fonts.googleapis.com/css2?family=Josefin+Sans:wght@300&family=Open+Sans:wght@400&family=Parisienne&family=Roboto+Condensed:wght@400;700&display=swap">
<style>
  :root {
    --paper: #ffffff;
    --charcoal-top: #4b5557;
    --charcoal-bottom: #1a1c1e;
    --sky: #3dbbea;
    --sky-deep: #35aee0;
    --aqua: #62e6f5;
    --gold: #d9ac3a;
    --gold-light: #e9cd7f;
    --ink: #1f1f1f;
    --rule: #2b2b2b;
    --white: #ffffff;
  }
  html, body {
    margin: 0;
    padding: 0;
    width: 1200px;
    height: 653px;
    overflow: hidden;
    background: var(--paper);
  }
  .card {
    display: block;
    width: 1200px;
    height: 653px;
  }
  .services {
    font-family: "Open Sans", sans-serif;
    font-size: 25px;
    fill: var(--white);
  }
  .contact {
    font-family: "Roboto Condensed", sans-serif;
    font-weight: 700;
    font-size: 19px;
    fill: var(--white);
  }
  .phone {
    font-family: "Roboto Condensed", sans-serif;
    font-weight: 700;
    font-size: 30px;
    fill: var(--white);
    letter-spacing: 1px;
  }
  .brand-name {
    font-family: "Josefin Sans", sans-serif;
    font-weight: 300;
    font-size: 56px;
    letter-spacing: 3px;
    fill: var(--ink);
  }
  .tagline {
    font-family: "Parisienne", cursive;
    font-size: 30px;
    fill: var(--ink);
  }
  .logo-name {
    font-family: "Josefin Sans", sans-serif;
    font-weight: 300;
    font-size: 22px;
    fill: var(--gold);
  }
</style>
</head>
<body>
<svg class="card" viewBox="0 0 980 533" width="1200" height="653" xmlns="http://www.w3.org/2000/svg">
  <defs>
    <linearGradient id="charcoal" x1="0" y1="0" x2="0" y2="1">
      <stop offset="0" stop-color="var(--charcoal-top)"/>
      <stop offset="1" stop-color="var(--charcoal-bottom)"/>
    </linearGradient>
  </defs>

  <!-- panels -->
  <rect class="paper" x="0" y="0" width="980" height="533" fill="var(--paper)"/>
  <polygon class="dark-panel" points="0,0 668,0 598,533 0,533" fill="url(#charcoal)"/>
  <rect class="contact-band" x="65" y="0" width="113" height="533" fill="var(--sky)"/>
  <polygon class="stripe-deep" points="668,0 712,0 655,368 611,368" fill="var(--sky-deep)"/>
  <polygon class="stripe-aqua" points="712,0 752,0 702,268 663,268" fill="var(--aqua)"/>
  <polygon class="stripe-foot" points="600,386 670,386 670,533 597,533" fill="var(--aqua)"/>

  <!-- phone -->
  <text class="phone" transform="translate(672 80) rotate(90)">0437260000</text>

  <!-- services -->
  <g class="services">
    <text transform="translate(547 55) rotate(90)">Pet Minding</text>
    <text transform="translate(509 55) rotate(90)">Puppy Classes</text>
    <text transform="translate(472 55) rotate(90)">Private Lessons</text>
    <text transform="translate(434 55) rotate(90)">Certified Dog Trainer</text>
    <text transform="translate(397 55) rotate(90)">Basic Obedience Classes</text>
    <text transform="translate(359 55) rotate(90)">Intermediate Obedience Classes</text>
    <text transform="translate(322 55) rotate(90)">CDTQ Certified Police Checked</text>
    <text transform="translate(284 55) rotate(90)">Mobile Dog Wash and Grooming</text>
    <text transform="translate(247 55) rotate(90)">Fully Insured Honest &amp; Reliable</text>
  </g>

  <!-- contact -->
  <rect class="social-square" x="135" y="133" width="38" height="38" fill="var(--white)"/>
  <g class="contact">
    <text transform="translate(150 185) rotate(90)" textLength="305" lengthAdjust="spacingAndGlyphs">www.socialnook.example/merrilymutts</text>
    <text transform="translate(110 185) rotate(90)" textLength="305" lengthAdjust="spacingAndGlyphs">merrilymutts@postlark.example</text>
    <text transform="translate(71 185) rotate(90)" textLength="285" lengthAdjust="spacingAndGlyphs">merrilymutts.example.au</text>
  </g>

  <!-- logo area -->
  <g class="logo" role="img" aria-label="Merrily Mutts logo">
    <circle class="logo-dot" cx="900" cy="62" r="46" fill="var(--gold-light)"/>
    <text class="logo-name" transform="translate(812 18) rotate(90)">Merrily Mutts</text>
  </g>
  <line class="rule" x1="772" y1="178" x2="980" y2="178" stroke="var(--rule)" stroke-width="1.5"/>

  <!-- name -->
  <text class="brand-name" transform="translate(883 215) rotate(90)">MERRILY</text>
  <text class="brand-name" transform="translate(809 215) rotate(90)">MUTTS</text>

  <!-- tagline -->
  <text class="tagline" transform="translate(752 190) rotate(90)">“Life is merrier with mutts”</text>
</svg>
</body>
</html>
```